Economics of an Assumption vs Obtaining a New Loan at Current Market Rate

I need to marketing flyer that has fields that calculate mortgage payments amongst other calculations. I have a rough draft that I will attach.

The idea is to provide a tool for a real estate agent to use to illustrate to a potential buyer what a payment would be if they assumed the existing loan on the house or took out a new loan at current market.

The flyer needs to be able to allow an agent to drop in their logo, photo, and contact along with the loan officers photo and contact info.

You can google open house flyer to see examples of what the overall artwork and presentation can look like.

Target Market(s)

Home Buyers

Industry/Entity Type

Real Estate

Colors
F0912C
F2A743
F7CA91
FBE8D2
FDF5EE
EE7325
F08F49
F5BC92
FAE3D3
FDF4ED

Requirements
Must have
• A way to calculate mortgage payment
Nice to have
• Photo and logo drop ins

```html
<!DOCTYPE html>
<html lang="en">
<head>
<meta charset="utf-8">
<title>Assumption vs New Loan Flyer</title>
<link rel="stylesheet" href="https://fonts.googleapis.com/css2?family=Bebas+Neue&family=Montserrat:wght@400;500;600&display=swap">
<style>
  :root{
    --stage:#1b1c1e;
    --paper:#ffffff;
    --paper-soft:#f6fbfd;
    --aqua:#5cc4dd;
    --aqua-deep:#3fb3d1;
    --aqua-mid:#9fdcec;
    --aqua-light:#d7f1f8;
    --aqua-pale:#eef9fc;
    --orange:#f0912c;
    --ink:#1e1e1e;
    --ink-soft:#333;
  }
  *{box-sizing:border-box;margin:0;padding:0}
  html,body{width:1200px;height:1064px;overflow:hidden;background:var(--stage)}
  body{font-family:"Montserrat",Arial,sans-serif;color:var(--ink)}
  .flyer{
    position:absolute;left:210px;top:27px;width:780px;height:1010px;
    background:linear-gradient(180deg,var(--paper) 0%,var(--paper) 55%,var(--aqua-light) 85%,var(--aqua) 100%);
    overflow:hidden;
  }
  .flyer-inner{
    position:absolute;left:34px;right:34px;top:0;bottom:34px;
    background:linear-gradient(180deg,transparent 0%,var(--paper) 70%,var(--paper-soft) 100%);
    border-radius:0 0 40px 40px;
  }
  .hero-frame{position:absolute;left:60px;top:40px;width:700px;height:470px}
  .brand{position:absolute;left:60px;top:120px;display:flex;align-items:center;gap:14px}
  .brand-mark{width:30px;height:30px;border-radius:50%;background:var(--orange)}
  .brand-name{font-size:58px;font-weight:400;color:var(--orange);letter-spacing:1px;line-height:1}
  .price-tag{position:absolute;left:560px;top:28px;width:170px;height:118px}
  .price-tag-text{position:absolute;left:560px;top:42px;width:170px;text-align:center;color:#fff}
  .price-label{font-size:15px;font-weight:500;letter-spacing:.5px}
  .price-value{font-family:"Bebas Neue",Impact,sans-serif;font-size:32px;line-height:1}
  .panel{
    position:absolute;border-radius:30px;
    background:linear-gradient(180deg,var(--aqua-mid) 0%,var(--aqua-light) 55%,rgba(255,255,255,.95) 100%);
    padding:22px 24px 18px;
  }
  .panel-current{left:140px;top:460px;width:330px;height:292px}
  .panel-new{left:472px;top:408px;width:300px;height:344px}
  .panel-title{font-family:"Bebas Neue",Impact,sans-serif;font-size:34px;letter-spacing:2px;line-height:1;color:var(--ink);margin-bottom:14px;display:flex;align-items:flex-end;gap:6px;white-space:nowrap}
  .panel-new .panel-title{font-size:30px;letter-spacing:1px}
  .panel-title small{font-family:"Montserrat",sans-serif;font-size:9px;line-height:1.05;letter-spacing:.5px;font-weight:500;padding-bottom:3px}
  .field-row{display:flex;align-items:center;justify-content:space-between;height:28px;font-size:12px;color:var(--ink-soft)}
  .field-row.tall{height:40px}
  .field-pill{width:120px;height:20px;border-radius:10px;background:#fff;box-shadow:inset 0 0 0 1px var(--aqua-light);font-size:9px;display:flex;align-items:center;justify-content:center;text-align:center;line-height:1.05;color:var(--ink)}
  .term-field{display:flex;align-items:center}
  .term-field .field-pill{width:106px}
  .split-row{display:flex;align-items:center;gap:8px;height:28px;font-size:12px;color:var(--ink-soft)}
  .split-row .field-pill{width:74px}
  .note{font-size:10px;color:var(--ink-soft)}
  .unit{font-size:9px;margin-left:4px}
  .difference-bar{
    position:absolute;left:250px;top:768px;width:430px;height:44px;border-radius:22px;
    background:linear-gradient(90deg,var(--aqua-light),var(--aqua-mid));
    display:flex;align-items:center;padding:0 10px 0 24px;gap:16px;font-size:17px;font-weight:500;color:var(--ink)
  }
  .difference-bar .field-pill{flex:1;height:24px;border-radius:12px}
  .certified{position:absolute;left:0;right:0;top:830px;text-align:center;font-size:19px;font-weight:600;color:var(--ink)}
  .drop-zones{position:absolute;left:110px;right:80px;top:870px;display:flex;justify-content:space-between}
  .drop-zone{display:flex;flex-direction:column;align-items:center;gap:8px;font-size:12px;color:var(--ink)}
  .drop-box{width:100px;height:72px;border-radius:14px;border:1.5px solid var(--aqua);background:#fff}
</style>
</head>
<body>
<main class="flyer">
  <div class="flyer-inner"></div>

  <svg class="hero-frame" viewBox="0 0 700 470" role="img" aria-label="Photo of a modern white two-storey house with glass balconies and a pool">
    <defs>
      <linearGradient id="heroFill" x1="0" y1="0" x2="0" y2="1">
        <stop offset="0" stop-color="#dfe7ee"/>
        <stop offset=".55" stop-color="#c9ccd0"/>
        <stop offset="1" stop-color="#8fd0e2"/>
      </linearGradient>
    </defs>
    <path d="M210 20 L560 20 L690 200 L690 470 L10 470 L10 250 L140 150 Z" fill="#e6f5fa"/>
    <path d="M222 34 L552 34 L676 204 L676 460 L22 460 L22 258 L150 162 Z" fill="url(#heroFill)"/>
  </svg>

  <div class="brand">
    <span class="brand-mark"></span>
    <span class="brand-name">Keyla</span>
  </div>

  <svg class="price-tag" viewBox="0 0 170 118" aria-hidden="true">
    <path d="M0 0 H170 V78 L85 118 L0 78 Z" fill="var(--aqua)"/>
  </svg>
  <div class="price-tag-text">
    <div class="price-label">Purchase Price</div>
    <div class="price-value">$1,2300,000</div>
  </div>

  <section class="panel panel-current">
    <h2 class="panel-title">Current Mortgage</h2>
    <div class="field-row"><span>Loan Amount</span><span class="field-pill"></span></div>
    <div class="field-row"><span>Interest Rate</span><span class="field-pill"></span></div>
    <div class="field-row"><span>Principal &amp; Interest</span><span class="field-pill"></span></div>
    <div class="field-row"><span>Mortgage Insurance</span><span class="field-pill"></span></div>
    <div class="field-row"><span>Total</span><span class="field-pill"></span></div>
    <div class="split-row"><span>Years</span><span class="field-pill"></span><span>Months</span><span class="field-pill"></span></div>
    <div class="split-row"><span>Delta</span><span class="note">Purchase Price minus Loan Amount</span></div>
  </section>

  <section class="panel panel-new">
    <h2 class="panel-title">New Mortgage 10% <small>DOWN<br>PAYMENT</small></h2>
    <div class="field-row"><span>Loan Amount</span><span class="field-pill">90% of Purchase Price</span></div>
    <div class="field-row"><span>Interest Rate</span><span class="field-pill">Input</span></div>
    <div class="field-row"><span>Principal &amp; Interest</span><span class="field-pill">Calc Payment</span></div>
    <div class="field-row"><span>Mortgage Insurance</span><span class="field-pill">Input %</span></div>
    <div class="field-row"><span>Total</span><span class="field-pill">Principal + Mortgage<br>Insurance&nbsp;&nbsp;Insurance</span></div>
    <div class="field-row"><span>Term</span><span class="term-field"><span class="field-pill">Input</span><span class="unit">Yrs</span></span></div>
    <div class="field-row tall"><span>Down Payment<br>Amount</span><span class="field-pill"></span></div>
  </section>

  <div class="difference-bar"><span>Payment Difference</span><span class="field-pill"></span></div>

  <p class="certified">This Property is " Easy Rate Advantage Certified"</p>

  <div class="drop-zones">
    <div class="drop-zone"><span class="drop-box"></span><span>Drop Photo</span></div>
    <div class="drop-zone"><span class="drop-box"></span><span>Drop Contact Info</span></div>
    <div class="drop-zone"><span class="drop-box"></span><span>Drop Contact Info</span></div>
    <div class="drop-zone"><span class="drop-box"></span><span>Drop Logo</span></div>
  </div>
</main>
</body>
</html>
```